Professional, Attractive, Simple Website Needed!!

We completed the design for our logo.

We need a website built out around this.

Here are a couple samples of how we want ours formatted.

http://brvntapower.com

http://www.halvorbeam.com/lp/free-quote?LeadSource=Search%20Engine&ProgramName=webquery&experience=qual&language=en&type=brd&gclid=Xq7RTPwmEYKDLAvUHbsNQkfPZrTcGwnJuoVbXeLqHmRYdAsWtPkMcNfBYgzTrUoQJhEdWvKpYaLsZbCmNDgQwTxAoKpXbT_qkR

http://morvalo.co

Reason: Extending this deadline due to our delay in providing designers with content for each page. This is coming in next 24 hours.

Reason: Due to scheduling conflicts and extended travel delays related to Puerto Rico, the deadline has been extended. Your patience is greatly appreciated.

Reason: Travel and scheduling conflicts have made it impossible to give this project the thorough review it deserves, therefore I am extending the deadline. Thank you for your patience!

Target Market(s)

Home Owners who earn 60k + household annually

Industry/Entity Type

It Professional

Coding

Coded - Design and coding required

Number of Pages Required

5+ page

Font styles to use
Serif

Colors
34a7d8
9bcb3c

Requirements
Must have
• Simple
• Lead form Entry (Ability for visitor to enter Name, number and address for a quote)
• Sleek Design
• Professional
• Testimonials
• Use color Scheme of Design Logo Attached
Nice to have
• Video when site starts
• Like this
• https://www.vidmarrow.com/watch?v=qT8mRpXw2Ka&feature=vidm.ro
Should not have
• Should not include Commercial solar
• Should not include wind power

```html
<!DOCTYPE html>
<html lang="en">
<head>
<meta charset="utf-8">
<title>Bright Acre Energy</title>
<link rel="stylesheet" href="https://fonts.googleapis.com/css2?family=Montserrat:wght@500;700;800&family=Raleway:wght@400;500;600&display=swap">
<style>
:root{
  --green:#8dc63f;
  --blue:#34a7d8;
  --slate:#363a42;
  --slate-panel:#3b3f47;
  --panel-glass:rgba(54,58,66,.93);
  --white:#ffffff;
  --muted:#d9dadc;
  --page:#ffffff;
}
*{box-sizing:border-box;margin:0;padding:0}
html,body{width:1200px;height:1200px;overflow:hidden;background:var(--page)}
body{font-family:"Raleway",sans-serif;color:var(--white)}
.site{position:absolute;left:112px;top:0;width:976px;height:1200px;overflow:hidden;background:var(--slate)}
.abs{position:absolute}

/* hero */
.hero-photo{left:0;top:0;width:976px;height:490px;
  background:linear-gradient(125deg,#0d1a33 0%,#1c3a66 30%,#2a5288 48%,#16305a 62%,#4a6a86 80%,#1a2a3a 100%)}
.brand{left:104px;top:14px;display:flex;align-items:center;gap:6px}
.brand-dot{width:20px;height:20px;border-radius:50%;background:var(--green)}
.brand-name{font-family:"Montserrat",sans-serif;font-weight:700;font-size:12px;color:var(--green);letter-spacing:.5px;line-height:1.1}
.nav{top:22px;left:578px;display:flex;align-items:center;font-size:10px;font-weight:500}
.nav a{color:var(--white);text-decoration:none;margin-right:24px}
.nav .nav-cta{background:var(--green);padding:9px 12px;margin:0 0 0 -3px}

.lead-form{left:619px;top:79px;width:263px;height:331px;background:var(--panel-glass);padding:14px 12px}
.lead-form h2{font-family:"Montserrat",sans-serif;font-weight:800;font-size:13.5px;line-height:18px;text-transform:uppercase;letter-spacing:-.2px}
.field{display:block;width:238px;height:26px;background:var(--white);margin-top:17.5px;color:#a8a8a8;font-size:9px;padding:7px 7px;position:relative}
.field:first-of-type{margin-top:13px}
.field.select{color:#444}
.field.select::after{content:"▾";position:absolute;right:6px;top:7px;font-size:8px}
.submit{margin-top:15px;width:238px;height:27px;background:var(--green);text-align:center;font-family:"Montserrat",sans-serif;font-weight:500;font-size:9.5px;letter-spacing:.8px;line-height:27px}

/* features */
.features{left:0;top:490px;width:976px;height:198px;background:var(--slate)}
.feature{width:326px;text-align:center}
.badge{position:absolute;width:100px;height:100px;border-radius:50%;background:var(--slate);border:3px solid #cfd1d4;display:flex;align-items:center;justify-content:center}
.badge-inner{width:80px;height:80px;border-radius:50%;background:var(--white);display:flex;align-items:center;justify-content:center}
.feature h3{font-family:"Montserrat",sans-serif;font-weight:700;font-size:20.5px;letter-spacing:1.5px;text-transform:uppercase}
.feature p{font-size:9.5px;margin-top:9px}
.feature a{display:inline-block;margin-top:12px;font-size:9.5px;color:var(--green);text-decoration:none;border-bottom:1px dotted var(--green)}
.divider{width:0;border-left:1px dotted #5a8fb0;height:123px;top:528px}

/* green section */
.scene-photo{left:0;top:688px;width:976px;height:330px;
  background:linear-gradient(180deg,#1f4a3a 0%,#2f6a3a 30%,#5c8f3a 60%,#9fc04a 85%,#4e6a2a 100%)}
.story{left:42px;top:744px;width:391px;height:218px;background:var(--slate-panel);padding:16px 14px}
.story h2{font-family:"Montserrat",sans-serif;font-weight:700;font-size:25px;color:var(--green);letter-spacing:-.3px;line-height:28px}
.story p{margin-top:16px;font-size:9.4px;line-height:15px;color:var(--muted)}
.btn{position:absolute;top:174px;height:31px;font-family:"Montserrat",sans-serif;font-weight:500;font-size:9.5px;letter-spacing:1.2px;line-height:29px;text-align:center;border:1px solid var(--green)}
.btn-solid{left:13px;width:111px;background:var(--green)}
.btn-outline{left:136px;width:112px;color:var(--white)}

/* footer */
.footer{left:0;top:1018px;width:976px;height:182px;background:var(--slate);text-align:center}
.footer-brand{position:absolute;left:0;right:0;top:30px;display:flex;flex-direction:column;align-items:center;gap:8px}
.footer-brand .brand-dot{width:40px;height:40px}
.footer-brand .brand-name{font-size:15px}
.footer-links{position:absolute;left:0;right:0;top:106px;font-size:9.5px}
.footer-links a{color:var(--green);text-decoration:none;border-bottom:1px dotted var(--green);margin:0 10px}
.legal{position:absolute;left:0;right:0;top:136px;font-size:7.5px;line-height:15px}
</style>
</head>
<body>
<div class="site">
  <div class="abs hero-photo" role="img" aria-label="Close-up photograph of blue rooftop solar panels"></div>

  <div class="abs brand"><span class="brand-dot"></span><span class="brand-name">BRIGHT ACRE<br>ENERGY</span></div>
  <nav class="abs nav"><a href="#">How It Works</a><a href="#">Why Bright Acre Energy</a><a class="nav-cta" href="#">Get Started</a></nav>

  <form class="abs lead-form">
    <h2>Save big on your electric bill.<br>See if you qualify now!</h2>
    <span class="field">Full Name</span>
    <span class="field">Phone Number</span>
    <span class="field">Email Address</span>
    <span class="field">Zip Code</span>
    <span class="field select">Do you own your home?</span>
    <div class="submit">GET STARTED TODAY!</div>
  </form>

  <section class="abs features"></section>
  <div class="abs divider" style="left:322px"></div>
  <div class="abs divider" style="left:654px"></div>

  <div class="badge" style="left:103px;top:434px"><div class="badge-inner">
    <svg width="50" height="40" viewBox="0 0 50 40"><g fill="none" stroke-width="2.5"><circle cx="15" cy="20" r="12" stroke="#34a7d8"/><path d="M26 9h20M27 15h19M28 21h18M27 27h19M26 33h20" stroke="#8dc63f"/></g><text x="15" y="26" text-anchor="middle" font-family="Montserrat,sans-serif" font-weight="700" font-size="16" fill="#34a7d8">$</text></svg>
  </div></div>
  <div class="badge" style="left:437px;top:448px"><div class="badge-inner">
    <svg width="44" height="44" viewBox="0 0 44 44"><g stroke="#34a7d8" stroke-width="2.5" stroke-linecap="round"><path d="M22 3v5M6 20h5M33 20h5M10 8l3 3M34 8l-3 3M10 32l3-3M34 32l-3-3"/></g><path d="M22 12a8 8 0 0 0-5 14v4h10v-4a8 8 0 0 0-5-14z" fill="#34a7d8"/><rect x="18" y="32" width="8" height="5" rx="1" fill="#8dc63f"/></svg>
  </div></div>
  <div class="badge" style="left:772px;top:434px"><div class="badge-inner">
    <svg width="44" height="44" viewBox="0 0 44 44"><path d="M8 6a8 8 0 0 0 9 11l18 18a3 3 0 0 0 4-4L21 13A8 8 0 0 0 10 4l5 5-2 4-4 2z" fill="#34a7d8"/><path d="M14 30l8-8 4 4-8 8z" fill="#8dc63f"/></svg>
  </div></div>

  <div class="abs feature" style="left:-10px;top:545px"><h3>Zero Cost</h3><p>Most of our customers qualify for zero out-of-pocket costs.</p><a href="#">Apply Now</a></div>
  <div class="abs feature" style="left:324px;top:559px"><h3>Energy Efficient</h3><p>Save money on your electric bills by going solar.</p><a href="#">Go Green</a></div>
  <div class="abs feature" style="left:659px;top:545px"><h3>Maintenance Free</h3><p>If something goes wrong, don't worry, it's covered.</p><a href="#">Get Started</a></div>

  <div class="abs scene-photo" role="img" aria-label="Photograph of a green hillside village with solar panels on a house roof beside a pond"></div>
  <section class="abs story">
    <h2>GO GREEN, GET GREEN</h2>
    <p>Lorem ipsum dolor sit amet, consectetur adipiscing elit. Ut id dignissim mi, vel rhoncus libero. Suspendisse at nibh at neque feugiat viverra. Phasellus convallis augue a gravida rutrum. Integer pulvinar arcu quis quam aliquam, vehicula gravida metus faucibus. Integer sed rutrum sapien. Vestibulum nec condimentum ligula. Proin quis ligula interdum, sagittis tortor at, ullamcorper nisl. Morbi aliquam turpis est, non tristique massa mollis eget. Sed fermentum ullamcorper enim, sit amet fringilla risus cursus eu. Nulla vehicula mi ac justo accumsan suscipit.</p>
    <span class="btn btn-solid">LEARN MORE</span>
    <span class="btn btn-outline">GET STARTED</span>
  </section>

  <footer class="abs footer">
    <div class="footer-brand"><span class="brand-dot"></span><span class="brand-name">BRIGHT ACRE ENERGY</span></div>
    <div class="footer-links"><a href="#">News</a><a href="#">Careers</a><a href="#">Privacy Policy</a></div>
    <div class="legal">© Copyright 2017 Bright Acre Energy<br>All Rights Reserved</div>
  </footer>
</div>
</body>
</html>
```